christmas trees postcard design

wales largest grower of christmas trees, suppling freshly cut perfect christmas trees, wholesale, retail businesses and nmb 27 marlow terrace! Our focus in nurturing the perfect christmas tree from seed for 10 years , and providing a fresh long lasting christmas tree which lasts the festive period, trees from 2 ft to 20ft , many varieties sixzes and shapes

```html
<!DOCTYPE html>
<html lang="en">
<head>
<meta charset="utf-8">
<title>Valley Pine Farm Postcard</title>
<link href="https://fonts.googleapis.com/css2?family=Open+Sans:wght@600;700&family=PT+Sans+Narrow:wght@400;700&display=swap" rel="stylesheet">
<style>
  :root{
    --page:#e9e4dd;
    --band:rgba(46,140,78,.85);
    --ribbon:#3cb049;
    --ribbon-dark:#1f7a2c;
    --lime:#9ed43a;
    --ink:#1d1d1b;
    --forest:#1d5a2a;
    --white:#ffffff;
    --snow-top:#6d7a6f;
    --snow-bottom:#f1f2f0;
  }
  *{box-sizing:border-box;margin:0;padding:0}
  html,body{width:1200px;height:1200px;overflow:hidden;background:var(--page)}
  .postcard{position:absolute;left:272px;width:696px;box-shadow:0 3px 10px rgba(0,0,0,.25);overflow:hidden}
  .postcard--front{top:44px;height:538px}
  .postcard--back{top:614px;height:539px;background:linear-gradient(#fff,#e4e4e4)}
  .photo{position:absolute;inset:0}
  .photo--snow-field{background:linear-gradient(180deg,#4a5650 0%,#7b857d 25%,#56625a 45%,#a9afa8 70%,var(--snow-bottom) 100%)}
  .photo--pine-rows{background:linear-gradient(180deg,#b9cbbb,#9fb9a2 50%,#aec2ae);}
  .band{position:absolute;left:0;right:0;top:195px;height:148px;background:var(--band);border-top:1px solid rgba(255,255,255,.4);border-bottom:1px solid rgba(255,255,255,.4)}
  .ribbon{position:absolute}
  .ribbon svg{position:absolute;inset:0;width:100%;height:100%}
  .ribbon__name{position:absolute;inset:0;display:flex;align-items:center;justify-content:center;font-family:'Open Sans',sans-serif;font-weight:700;color:var(--white)}
  .front .ribbon{left:120px;top:208px;width:456px;height:64px}
  .front .ribbon__name{font-size:30px}
  .tagline{position:absolute;left:0;right:0;text-align:center;font-family:'Open Sans',sans-serif;font-weight:600;color:var(--white)}
  .tagline--main{top:282px;font-size:20px}
  .tagline--sub{top:308px;font-size:16.5px}
  .tagline--sub .hl{color:var(--lime)}
  .info-box{position:absolute;left:114px;top:360px;width:467px;height:44px;background:rgba(255,255,255,.75);font-family:'PT Sans Narrow',sans-serif;font-size:11.5px;line-height:16px;color:var(--ink);text-align:center;padding-top:6px}
  .web{position:absolute;left:0;right:0;text-align:center;font-family:'PT Sans Narrow',sans-serif;font-weight:700;color:var(--forest)}
  .front .web{top:410px;font-size:15px}
  .back-info{position:absolute;left:0;top:0;width:336px;height:539px;overflow:hidden}
  .back-info .veil{position:absolute;inset:0;background:rgba(255,255,255,.55)}
  .back-info .ribbon{left:24px;top:26px;width:296px;height:42px}
  .back-info .ribbon__name{font-size:19px}
  .back-title{position:absolute;left:0;right:0;top:88px;text-align:center;font-family:'PT Sans Narrow',sans-serif;font-weight:700;font-size:19px;color:var(--ink)}
  .back-intro{position:absolute;left:30px;right:14px;top:114px;text-align:center;font-family:'PT Sans Narrow',sans-serif;font-size:11.5px;line-height:16px;color:var(--ink)}
  .feature-list{list-style:none;position:absolute;left:0;right:0;top:0}
  .feature{position:absolute;left:0;right:0;text-align:center;font-family:'PT Sans Narrow',sans-serif;font-size:14.5px;line-height:20px;color:var(--ink)}
  .feature svg{display:block;margin:0 auto 4px;width:12px;height:18px}
  .divider{position:absolute;left:56px;width:216px;top:450px;border-top:1px solid rgba(255,255,255,.9)}
  .social{position:absolute;top:462px;width:30px;height:30px;border-radius:50%;background:var(--white)}
  .back-info .web{top:500px;font-size:15px}
  .address-side{position:absolute;left:336px;top:0;right:0;bottom:0}
  .stamp-box{position:absolute;left:216px;top:16px;width:128px;height:128px;background:var(--white);border:1px solid #d6d6d6}
  .address-line{position:absolute;left:24px;width:314px;border-top:1px dotted #8a8a8a}
</style>
</head>
<body>
<svg width="0" height="0" style="position:absolute">
  <defs>
    <symbol id="tree" viewBox="0 0 12 18"><path d="M6 0 9 6H7.5L10.5 11H8.5L12 16H0L3.5 11H1.5L4.5 6H3Z" fill="#1f7a2c"/><rect x="5" y="16" width="2" height="2" fill="#1f7a2c"/></symbol>
    <symbol id="ribbon-shape" viewBox="0 0 456 64" preserveAspectRatio="none">
      <polygon points="0,22 56,22 56,56 0,56 12,39" fill="#3cb049"/>
      <polygon points="456,22 400,22 400,56 456,56 444,39" fill="#3cb049"/>
      <polygon points="48,50 64,64 64,50" fill="#1f7a2c"/>
      <polygon points="408,50 392,64 392,50" fill="#1f7a2c"/>
      <polygon points="60,0 396,0 388,32 396,64 64,64 72,32" fill="#3cb049"/>
    </symbol>
  </defs>
</svg>

<section class="postcard postcard--front front">
  <div class="photo photo--snow-field" role="img" aria-label="Photograph of snow-covered rows of young Christmas trees on a hillside farm"></div>
  <div class="band"></div>
  <div class="ribbon">
    <svg><use href="#ribbon-shape"/></svg>
    <div class="ribbon__name">Valley Pine Farm</div>
  </div>
  <p class="tagline tagline--main">Largest Grower of Christmas Trees</p>
  <p class="tagline tagline--sub"><span class="hl">wholesale, retail businesses</span> and <span class="hl">nmb 27 marlow terrace!</span></p>
  <div class="info-box">We are providing a fresh long lasting christmas tree which lasts the festive period, trees from 2 ft to 20ft ,<br>many varieties sixzes and shapesshapes</div>
  <p class="web">www.valley-pine-farm.co.uk</p>
</section>

<section class="postcard postcard--back">
  <div class="back-info">
    <div class="photo photo--pine-rows" role="img" aria-label="Faded photograph of a path between rows of green Christmas trees"></div>
    <div class="veil"></div>
    <div class="ribbon">
      <svg><use href="#ribbon-shape"/></svg>
      <div class="ribbon__name">Valley Pine Farm</div>
    </div>
    <h2 class="back-title">Wales Largest Grower of Christmas Trees</h2>
    <p class="back-intro">A large retail site and Christmas grotto on my farm where we grow the trees 500,000 of them.</p>
    <ul class="feature-list">
      <li class="feature" style="top:160px"><svg><use href="#tree"/></svg>Suppling freshly cut perfect christmas trees</li>
      <li class="feature" style="top:210px"><svg><use href="#tree"/></svg>Wholesal</li>
      <li class="feature" style="top:263px"><svg><use href="#tree"/></svg>Retail businesses and nmb 27 marlow terrace!</li>
      <li class="feature" style="top:320px"><svg><use href="#tree"/></svg>Our focus in nurturing the perfect christmas tree<br>from seed for 10 years</li>
      <li class="feature" style="top:393px"><svg><use href="#tree"/></svg>Trees from 2 ft to 20ft</li>
    </ul>
    <div class="divider"></div>
    <span class="social" style="left:119px"></span>
    <span class="social" style="left:173px"></span>
    <p class="web">www.valley-pine-farm.co.uk</p>
  </div>
  <div class="address-side">
    <div class="stamp-box"></div>
    <div class="address-line" style="top:257px"></div>
    <div class="address-line" style="top:310px"></div>
    <div class="address-line" style="top:362px"></div>
    <div class="address-line" style="top:413px"></div>
  </div>
</section>
</body>
</html>
```